4 page A4 flyer/brochure needed to promote Ski & Snowboard courses

We need a flyer/brochure design for a family run company called Neige du Vent.
Neige du Vent is the original provider of ski and snowboard instructor training courses for the ultimate gap year experience. Based in Canada, our comprehensive courses enable students to gain a variety of internationally recognised qualifications with coaching from top level instructors that work exclusively for Neige du Vent.
Our motto is PLAY LEARN TEACH - students have a lot of fun. We have an extensive social programme including weekend trips around Canada, at the same time as learning to become an instructor. They also have the chance to put their newly acquired teaching skills into practice with work experience at the local snow school.
We have 3 different courses: the Summit Forge course, the Peak Horizon course and Improvement courses.
The majority of our students are between 18-25 years old so we would like the design to appeal to that target age, but remain modern and clear to read the information.
I have attached a file containing content and a selection of photos you may wish to use. I have also added our old flyer (but i am looking for something more modern) and a sketch of a layout idea for the inside pages.

Reason: Hi, terribly sorry i have been ill for the past few days so haven't been able to provide any feedback. I am extending the deadline and will provide feedback today so revisions can be made. Sorry for any inconvenience. Thanks, Henrietta

Target Market(s)

Gap year students aged 18 - 25 years, interested in snow sports.

Industry/Entity Type

Travel Industry

Font styles to use
Sans Serif

Requirements
Must have
• An overview of the courses we offer, and the compare courses table outlined in the document attached titled 'content'. Logo and contact details must be easily visible.
Nice to have
• Perhaps a quote from our snow director Gavin - again attached in the content document.

```html
<!DOCTYPE html>
<html lang="en">
<head>
<meta charset="utf-8">
<title>Neige du Vent brochure</title>
<link href="https://fonts.googleapis.com/css2?family=Open+Sans:wght@400;600;700;800&family=Oswald:wght@500;700&display=swap" rel="stylesheet">
<style>
:root{
  --stage:#2b2b2e;
  --navy:#123a72;
  --blue:#1f6fc4;
  --sky:#5aa8e6;
  --pale:#e8f2fb;
  --red:#d3202a;
  --ink:#2a3340;
  --tick:#e6b800;
  --white:#ffffff;
}
*{margin:0;padding:0;box-sizing:border-box}
html,body{width:896px;height:1200px;overflow:hidden;background:var(--stage);font-family:"Open Sans",sans-serif;color:var(--ink)}
.canvas{position:relative;width:896px;height:1200px}
.page{position:absolute;background:var(--white);overflow:hidden}
.spread-label{position:absolute;left:30px;font:600 11px "Open Sans",sans-serif;color:#cfd3d8;letter-spacing:1px}
.photo{position:absolute}
.brand{position:absolute;display:flex;align-items:center;gap:5px;font:700 10px "Open Sans",sans-serif;color:var(--white)}
.brand .mark{width:20px;height:20px;background:var(--red)}
.small{font-size:6.5px;line-height:1.45}
/* front left */
.cover-top{position:absolute;left:0;top:0;width:420px;height:118px;background:linear-gradient(135deg,var(--navy),var(--blue))}
.cover-title{position:absolute;left:80px;top:18px;width:320px;font:700 21px/1.1 "Oswald",sans-serif;color:var(--white);text-transform:uppercase}
.cover-intro{position:absolute;left:16px;top:76px;width:200px;color:var(--white)}
.course{position:absolute;left:0;width:420px;height:100px}
.course-tag{position:absolute;left:16px;top:6px;background:var(--blue);color:var(--white);font:700 8px "Open Sans",sans-serif;padding:3px 8px;text-transform:uppercase}
.course-text{position:absolute;left:16px;top:24px;width:225px}
/* front right */
.why-title{position:absolute;left:16px;top:50px;font:800 17px "Open Sans",sans-serif;color:var(--navy)}
.why-list{position:absolute;left:16px;top:126px;width:400px;list-style:none}
.why-list li{font-size:7px;line-height:1.55;padding-left:10px;position:relative}
.why-list li::before{content:"";position:absolute;left:0;top:3px;width:5px;height:5px;background:var(--red)}
.circle{position:absolute;width:62px;height:62px;border-radius:50%;border:3px solid var(--sky)}
.motto{position:absolute;font:800 14px "Open Sans",sans-serif;color:var(--blue);width:90px;text-align:center}
/* inside left */
.compare-head{position:absolute;left:14px;top:12px;display:flex;align-items:center;gap:10px}
.compare-head .mark{width:26px;height:26px;background:var(--red)}
.compare-head h2{font:800 15px "Open Sans",sans-serif;color:var(--navy);text-transform:uppercase}
.contact{position:absolute;left:250px;top:12px;width:160px;font-size:6.5px;line-height:1.4}
table{position:absolute;left:10px;top:52px;width:400px;border-collapse:collapse;font-size:6.6px}
th{background:var(--navy);color:var(--white);font-weight:700;padding:4px;text-align:left}
td{padding:2.6px 4px;border-bottom:1px solid #dde6ef}
tr:nth-child(even) td{background:var(--pale)}
td.c{text-align:center;color:var(--tick);font-weight:800;font-size:9px;line-height:1}
/* inside right */
.director-title{position:absolute;left:180px;top:60px;font:800 20px "Open Sans",sans-serif;color:var(--navy);text-transform:uppercase}
.director-text{position:absolute;left:180px;top:96px;width:220px}
.director-more{position:absolute;left:16px;top:256px;width:390px}
</style>
</head>
<body>
<div class="canvas">

  <!-- FRONT SPREAD -->
  <section class="page" style="left:30px;top:15px;width:420px;height:429px">
    <div class="cover-top"></div>
    <div class="brand" style="left:16px;top:16px"><span class="mark"></span></div>
    <div style="position:absolute;left:14px;top:40px;font:700 8px 'Open Sans',sans-serif;color:var(--white)">Neige du Vent</div>
    <h1 class="cover-title">Become a ski or snowboard instructor in Canada!</h1>
    <p class="cover-intro small">Neige du Vent is the original provider of instructor training for the ultimate gap year, with top coaches in Canada.</p>

    <div class="course" style="top:124px">
      <span class="course-tag">Summit Forge</span>
      <p class="course-text small">Eleven weeks of coaching towards recognised ski and snowboard instructor qualifications, with shadowing and exam preparation at the local snow school alongside a full social programme.</p>
      <div class="photo" role="img" aria-label="Photo of students skiing together on a groomed slope" style="left:256px;top:4px;width:150px;height:88px;background:linear-gradient(135deg,#bcd7ef,#6e9cc6)"></div>
    </div>
    <div class="course" style="top:226px">
      <span class="course-tag">Peak Horizon</span>
      <p class="course-text small">A shorter season packed with coaching, freestyle and backcountry days, plus trips across Canada, ideal for riders who want qualifications and adventure.</p>
      <div class="photo" role="img" aria-label="Photo of a group posing in the snow" style="left:256px;top:4px;width:150px;height:88px;background:linear-gradient(135deg,#d9e6f2,#8fb0cf)"></div>
    </div>
    <div class="course" style="top:328px">
      <span class="course-tag">Improvement courses</span>
      <p class="course-text small">Flexible coaching weeks to sharpen technique on every kind of terrain, open to all levels who want to progress faster with expert guidance.</p>
      <div class="photo" role="img" aria-label="Photo of a skier carving on a snowy run" style="left:256px;top:4px;width:150px;height:88px;background:linear-gradient(135deg,#e4eef7,#7fa6c9)"></div>
    </div>
  </section>

  <section class="page" style="left:450px;top:15px;width:420px;height:429px;background:var(--pale)">
    <div class="photo" role="img" aria-label="Photo of an instructor in goggles and a red jacket" style="left:170px;top:0;width:250px;height:118px;background:linear-gradient(135deg,#6f9ecb,#c0392b)"></div>
    <h2 class="why-title">WHY NEIGE DU VENT ?</h2>
    <ul class="why-list">
      <li>Over 20 years of experience running instructor courses</li>
      <li>Internationally recognised qualifications with top coaches</li>
      <li>Small groups and coaching from our own instructors</li>
      <li>Work experience teaching at the local snow school</li>
      <li>Weekend trips and a full social programme across Canada</li>
      <li>Friendly family run company looking after every student</li>
    </ul>
    <div class="circle" role="img" aria-label="Photo of students having fun in the snow" style="left:45px;top:232px;background:linear-gradient(135deg,#d9e6f2,#8fb0cf)"></div>
    <div class="circle" role="img" aria-label="Photo of an instructor teaching a child" style="left:180px;top:232px;background:linear-gradient(135deg,#e6eef5,#c0392b)"></div>
    <div class="circle" role="img" aria-label="Photo of a group learning on a slope" style="left:315px;top:232px;background:linear-gradient(135deg,#e0ebf5,#6e9cc6)"></div>
    <span class="motto" style="left:31px;top:300px">PLAY</span>
    <span class="motto" style="left:166px;top:300px">TEACH</span>
    <span class="motto" style="left:301px;top:300px">LEARN</span>
    <div class="photo" role="img" aria-label="Photo of a skier jumping above snowy mountains" style="left:0;top:326px;width:420px;height:103px;background:linear-gradient(180deg,#8fc0ec,#e8f2fb 70%,#ffffff)"></div>
  </section>
  <div class="spread-label" style="top:460px">- FRONT DESIGN -</div>

  <!-- INSIDE SPREAD -->
  <section class="page" style="left:30px;top:500px;width:420px;height:640px">
    <div class="compare-head"><span class="mark"></span><h2>Compare course</h2></div>
    <p class="contact">hello@neigeduvent.ca<br>www.neigeduvent.ca<br>Phone: +1 555 014 2290</p>
    <table>
      <thead><tr><th style="width:40%">Included</th><th>Summit Forge</th><th>Peak Horizon</th><th>Improvement</th></tr></thead>
      <tbody>
        <tr><td>Instructor qualification exam</td><td class="c">✓</td><td class="c">✓</td><td class="c"></td></tr>
        <tr><td>Airport transfers</td><td class="c">✓</td><td class="c">✓</td><td class="c">✓</td></tr>
        <tr><td>Chalet accommodation</td><td class="c">✓</td><td class="c">✓</td><td class="c">✓</td></tr>
        <tr><td>Breakfast, lunch and dinner</td><td class="c">✓</td><td class="c">✓</td><td class="c">✓</td></tr>
        <tr><td>Full season lift pass</td><td class="c">✓</td><td class="c">✓</td><td class="c"></td></tr>
        <tr><td>Daily coaching sessions</td><td class="c">✓</td><td class="c">✓</td><td class="c">✓</td></tr>
        <tr><td>Avalanche awareness</td><td class="c">✓</td><td class="c">✓</td><td class="c"></td></tr>
        <tr><td>Mountain first aid</td><td class="c">✓</td><td class="c"></td><td class="c"></td></tr>
        <tr><td>Freestyle park coaching</td><td class="c">✓</td><td class="c">✓</td><td class="c">✓</td></tr>
        <tr><td>Backcountry day trips</td><td class="c">✓</td><td class="c">✓</td><td class="c"></td></tr>
        <tr><td>Snow school shadowing</td><td class="c">✓</td><td class="c"></td><td class="c"></td></tr>
        <tr><td>Video analysis</td><td class="c">✓</td><td class="c">✓</td><td class="c">✓</td></tr>
        <tr><td>Weekend trips</td><td class="c">✓</td><td class="c">✓</td><td class="c"></td></tr>
        <tr><td>Ice hockey night</td><td class="c">✓</td><td class="c">✓</td><td class="c"></td></tr>
        <tr><td>Social programme</td><td class="c">✓</td><td class="c">✓</td><td class="c">✓</td></tr>
        <tr><td>Equipment discounts</td><td class="c">✓</td><td class="c">✓</td><td class="c">✓</td></tr>
        <tr><td>Reference letter</td><td class="c">✓</td><td class="c"></td><td class="c"></td></tr>
        <tr><td>Work experience</td><td class="c">✓</td><td class="c"></td><td class="c"></td></tr>
        <tr><td>Progress reports</td><td class="c">✓</td><td class="c">✓</td><td class="c">✓</td></tr>
        <tr><td>Welcome pack</td><td class="c">✓</td><td class="c">✓</td><td class="c">✓</td></tr>
        <tr><td>Graduation party</td><td class="c">✓</td><td class="c">✓</td><td class="c"></td></tr>
        <tr><td>Season hoodie</td><td class="c">✓</td><td class="c">✓</td><td class="c"></td></tr>
        <tr><td>Staff on call 24/7</td><td class="c">✓</td><td class="c">✓</td><td class="c">✓</td></tr>
        <tr><td>Course length in weeks</td><td class="c">11</td><td class="c">6</td><td class="c">1+</td></tr>
        <tr><td>Video of your experience</td><td class="c">✓</td><td class="c">✓</td><td class="c"></td></tr>
      </tbody>
    </table>
  </section>

  <section class="page" style="left:450px;top:500px;width:420px;height:640px">
    <div class="photo" role="img" aria-label="Portrait photo of the snow director Gavin in ski clothing" style="left:16px;top:24px;width:150px;height:222px;background:linear-gradient(180deg,#b8d4ee,#5a86b5)"></div>
    <h2 class="director-title">Director</h2>
    <p class="director-text small">Gavin has been on skis since he could walk and has spent more than twenty seasons coaching instructors across Canada. He built Neige du Vent with his family to give young people a season that changes their lives, combining serious training with plenty of fun on and off the mountain. Every course is shaped by his passion for teaching.</p>
    <p class="director-more small">“Seeing students arrive nervous and leave as confident, qualified instructors is the best part of my job. Our coaches care about every rider, and the friendships made here last far beyond the final exam day.”</p>
    <div class="photo" role="img" aria-label="Photo of a skier spraying snow in bright sunshine" style="left:0;top:340px;width:420px;height:300px;background:linear-gradient(160deg,#1e5a9c,#8fc0ec 55%,#ffffff)"></div>
    <svg style="position:absolute;left:0;top:300px" width="420" height="80" viewBox="0 0 420 80" aria-hidden="true">
      <polygon points="0,40 420,0 420,18 0,58" fill="#123a72"/>
      <polygon points="0,58 420,18 420,24 0,64" fill="#d3202a"/>
    </svg>
  </section>
  <div class="spread-label" style="top:1160px">- INSIDE DESIGN -</div>

</div>
</body>
</html>
```